Professional law firm looking for new professional and eye-catching business card design

Law firm in need of new business card design using existing firm logo and firm colors on thick card stock. Firm colors are navy blue, cyan blue, and gray. Please use firm's logo either on the back of the card or on the front and back. I am looking for something eye-catching and resonating but also professional.

Target Market(s)

Law firm growth by attracting clients with professional, creative, and attractive business cards.

Industry/Entity Type

Legal/Law Firm

Contact Information for Business Card

Name: Derek T. Halloway, Esq., Address: 517 E. Quintley Blvd., P.O. Box 641, Tavares, FL 32790, Phone numbers: (352) 555-0187 Office, (352) 555-0142 Fax, email address: DerekH@hqlegalfx.com, website: www.HQLegalFX.com

Font styles to use
Other font styles liked:
• Font as close as possible to matching law firm logo.

Requirements
Must have
• Must have business card details and law firm logo with law firm colors.

```html
<!DOCTYPE html>
<html lang="en">
<head>
<meta charset="utf-8">
<title>Halloway &amp; Quill, P.A. — Business Card</title>
<link rel="stylesheet" href="https://fonts.googleapis.com/css2?family=Tinos:wght@400;700&display=swap">
<style>
  :root {
    --navy: #141f29;
    --cyan: #29a8e0;
    --gray: #a7a7a9;
    --paper: #ffffff;
    --ink: #111111;
    --edge: #c4c4c4;
  }
  * { margin: 0; padding: 0; box-sizing: border-box; }
  html, body {
    width: 1200px; height: 1000px; overflow: hidden;
    background: var(--paper);
    font-family: "Tinos", "Times New Roman", serif;
  }
  .canvas { position: relative; width: 1200px; height: 1000px; }

  .card-front {
    position: absolute; left: 185px; top: 14px;
    width: 830px; height: 474px;
    background: var(--paper);
    border: 1px solid var(--edge);
  }
  .name-bar {
    position: absolute; left: 0; top: 29px;
    width: 424px; height: 78px;
    background: var(--navy);
    color: #fff;
    font-weight: 700; font-size: 31px;
    padding-left: 42px; line-height: 76px;
  }
  .contact {
    position: absolute; left: 42px; top: 245px;
    font-size: 18px; color: var(--ink); line-height: 24px;
  }
  .contact .row { display: flex; }
  .contact .row + .row { margin-top: 12px; }
  .contact .label { white-space: pre; }
  .contact .value { white-space: pre; }

  .firm-mark {
    position: absolute;
    color: var(--cyan);
    font-weight: 400;
    white-space: nowrap;
    text-align: center;
  }
  .card-front .firm-mark { left: 480px; top: 222px; width: 330px; font-size: 34px; }

  .card-back {
    position: absolute; left: 185px; top: 512px;
    width: 830px; height: 488px;
    background: var(--navy);
  }
  .card-back .firm-mark { left: 190px; top: 224px; width: 450px; font-size: 44px; }
</style>
</head>
<body>
<div class="canvas">
  <section class="card-front">
    <div class="name-bar">Derek T. Halloway, Esq.</div>
    <div class="contact">
      <div class="row"><span class="label">Address:  </span><span class="value">517 E. Quintley Blvd., P.O. Box 641,
Tavares, FL 32790</span></div>
      <div class="row"><span class="label">Phone numbers: </span><span class="value">(352) 555-0187  (Office)
(352) 555-0142  (Fax)</span></div>
      <div class="row"><span class="label">Email address: </span><span class="value">DerekH@hqlegalfx.com</span></div>
      <div class="row"><span class="label">Website: </span><span class="value">www.HQLegalFX.com</span></div>
    </div>
    <div class="firm-mark">Halloway &amp; Quill, P.A.</div>
  </section>

  <section class="card-back">
    <div class="firm-mark">Halloway &amp; Quill, P.A.</div>
  </section>
</div>
</body>
</html>
```